PACKAGING DESIGN - HOT New Brand of Haircare

We are creating a NEW haircare brand that will need to stand out on retail shelves. This is a luxury product at an affordable price. We will look for designs for 2 different formulas - Shine Boosting Shampoo & Moisturizing Conditioner containing Argan Oil and the other will be a Nourishing Shampoo & Hydrating Conditioner containing Coconut Oil.Packaging will be 32 oz bottle with pump (either Boston Round or Bullet shape). Examples are shown on the brief. This product will be sold at national retailers and needs to look like a brand that is sold at a high end boutique or salon.
Updates

Need extra days to review

Target Market(s)

Women and Men 20s - 40s who want high end hair care

Font styles to use
Sans Serif

Colors

Designer to choose colors to be used in the design.

Requirements
Must have
• Label design for the existing bottle - 4 different SKUs. (see attached brief)

```html
<!DOCTYPE html>
<html lang="en">
<head>
<meta charset="utf-8">
<title>Shampoo Back Label</title>
<link rel="stylesheet" href="https://fonts.googleapis.com/css2?family=Oswald:wght@500;600&family=Roboto+Condensed:wght@400&display=swap">
<style>
  :root {
    --label-brown: #673a13;
    --frame-blue: #0a1af5;
    --frame-white: #ffffff;
    --text-cream: #f4eee6;
    --upc-ink: #0b0b0b;
  }
  html, body {
    margin: 0;
    padding: 0;
    overflow: hidden;
  }
  .label {
    position: relative;
    width: 1200px;
    height: 2338px;
    background: var(--label-brown);
    overflow: hidden;
    color: var(--text-cream);
    font-family: "Roboto Condensed", "Arial Narrow", sans-serif;
  }
  .frames {
    position: absolute;
    inset: 0;
  }
  .brand-mark {
    position: absolute;
    left: 174px;
    top: 199px;
    width: 205px;
    height: 294px;
    background: radial-gradient(ellipse at 50% 45%, #2a3cf0 0%, #1522b8 55%, #3a2a1a 100%);
    border-radius: 40% 40% 50% 50% / 35% 35% 65% 65%;
  }
  .section-title {
    position: absolute;
    margin: 0;
    font-family: "Oswald", "Arial Narrow", sans-serif;
    font-weight: 500;
    font-size: 44px;
    line-height: 1;
    letter-spacing: 0;
    text-transform: uppercase;
  }
  .section-body {
    position: absolute;
    margin: 0;
    font-size: 42px;
    line-height: 67px;
  }
  .section-body span {
    display: block;
    white-space: nowrap;
  }
  .benefits-title { left: 459px; top: 197px; }
  .benefits-body { left: 459px; top: 252px; }
  .use-title { left: 166px; top: 556px; }
  .use-body { left: 166px; top: 612px; }
  .ingredients-title { left: 166px; top: 915px; }
  .ingredients-body { left: 166px; top: 972px; }
  .recycle-icon {
    position: absolute;
    left: 66px;
    top: 2026px;
    width: 233px;
    height: 272px;
  }
  .upc-box {
    position: absolute;
    left: 700px;
    top: 2040px;
    width: 432px;
    height: 266px;
    background: var(--frame-white);
    display: flex;
    align-items: center;
    justify-content: center;
  }
  .upc-text {
    font-family: "Oswald", "Arial Narrow", sans-serif;
    font-weight: 600;
    font-size: 150px;
    line-height: 1;
    color: var(--upc-ink);
  }
</style>
</head>
<body>
<main class="label">
  <svg class="frames" width="1200" height="2338" viewBox="0 0 1200 2338" aria-hidden="true">
    <rect x="63" y="63" width="1001" height="1859" fill="none" stroke="var(--frame-blue)" stroke-width="21"/>
    <rect x="96" y="94" width="1997" height="1874" fill="none" stroke="none"/>
    <rect x="96" y="94" width="997" height="1874" fill="none" stroke="var(--frame-white)" stroke-width="11"/>
    <rect x="135" y="152" width="1000" height="1861" fill="none" stroke="var(--frame-blue)" stroke-width="21"/>
    <rect x="158" y="176" width="887" height="1728" fill="var(--label-brown)" stroke="var(--frame-blue)" stroke-width="11"/>
  </svg>

  <div class="brand-mark" role="img" aria-label="Blue heart emblem with a water droplet"></div>

  <h2 class="section-title benefits-title">Benefits</h2>
  <p class="section-body benefits-body">
    <span>Cleanses and helps maintain</span>
    <span>an ideal moisture balance to</span>
    <span>promote healthy-looking and</span>
    <span>manageable hair.</span>
  </p>

  <h2 class="section-title use-title">Suggested Use</h2>
  <p class="section-body use-body">
    <span>Massage through wet hair and scalp. Rinse</span>
    <span>thoroughly. Add more water to activate a rich</span>
    <span>lather. Follow with Argan Bloom Moisturizing</span>
    <span>Conditioner.</span>
  </p>

  <h2 class="section-title ingredients-title">Ingredients</h2>
  <p class="section-body ingredients-body">
    <span>Water/Eau (Aqua), Sodium C14-16 Olefin</span>
    <span>Sulfonate, Cocamidopropyl Betaine, Cocamide</span>
    <span>Mea, Glycerin, Glycol Distearate, Fragrance/</span>
    <span>Parfum, Sodium Chloride, Argania Spinosa</span>
    <span>Kernel Oil (Argan Oil), Glycine Soja (Soybean)</span>
    <span>Protein, Hydrolyzed Keratin, Hydrolyzed Corn</span>
    <span>Protien, Hydrolyzed Soy Protein, Panthenol</span>
    <span>(Vitamin B5), Cyclopentasiloxane,</span>
    <span>Dimethiconol. Polyquaternium-10, PEG-150</span>
    <span>Distearate, Dicaprylyl Ether, Decyl Glucoside,</span>
    <span>Glyceryl Oleate, Phenoxytheanol,</span>
    <span>Methylchloroisothiazolinone,</span>
    <span>Methylisothiazolinone, Citric Acid,</span>
    <span>Polyquaternium-7.</span>
  </p>

  <svg class="recycle-icon" viewBox="0 0 233 272" role="img" aria-label="Recycling symbol">
    <g fill="var(--frame-blue)">
      <polygon points="116,20 160,95 135,95 116,62 90,108 62,92"/>
      <polygon points="175,115 215,185 170,250 158,225 190,185 160,135"/>
      <polygon points="40,140 72,160 50,200 120,200 120,230 20,230 10,210"/>
    </g>
  </svg>

  <div class="upc-box">
    <span class="upc-text">UPC</span>
  </div>
</main>
</body>
</html>
```